Fashion Design Business Card

I need a new business card designed for a new fashion company. I have attached what I have currently designed. I want it more feminine looking, the logo needs to be gold. I want it simple, feminine and stylish. Please give me some different ideas with the fonts.
Updates

I need to send the design we currently have, as we have worked out the logo.
You also need all of our details
Industry/Entity Type
Fashion
Look and feel
Each slider illustrates characteristics of the customer's brand and the style your logo design should communicate.

```html
<!DOCTYPE html>
<html lang="en">
<head>
<meta charset="utf-8">
<title>Marisol Devereux – Business Card</title>
<link rel="stylesheet" href="https://fonts.googleapis.com/css2?family=Cinzel:wght@400&family=Arimo:wght@400&display=swap">
<style>
  :root {
    --stage: #000000;
    --card-white: #ffffff;
    --card-yellow: #fedd1b;
    --ink-dark: #3a3a34;
    --ink-olive: #7d6f12;
  }
  * { margin: 0; padding: 0; box-sizing: border-box; }
  html, body {
    width: 1200px;
    height: 900px;
    overflow: hidden;
    background: var(--stage);
  }
  .canvas {
    position: relative;
    width: 1200px;
    height: 900px;
    background: var(--stage);
  }
  .card {
    position: absolute;
    top: 306px;
    width: 492px;
    height: 282px;
    border-radius: 12px;
    overflow: hidden;
    background: var(--card-yellow);
  }
  .card-front { left: 106px; }
  .card-back  { left: 638px; }

  .card-shape { position: absolute; inset: 0; }

  .serif { font-family: "Cinzel", "Times New Roman", serif; font-weight: 400; }
  .sans  { font-family: "Arimo", Arial, sans-serif; }

  /* front */
  .front-name {
    position: absolute;
    left: 0; right: 0; top: 104px;
    text-align: center;
    font-size: 19px;
    letter-spacing: 1px;
    white-space: nowrap;
    color: var(--ink-dark);
  }
  .front-identity {
    position: absolute;
    left: 30px; top: 216px;
    color: var(--ink-olive);
    white-space: nowrap;
  }
  .front-identity .person {
    font-size: 15px;
    letter-spacing: 0.8px;
    line-height: 1.15;
  }
  .front-identity .role {
    font-size: 8.5px;
    letter-spacing: 0.6px;
  }
  .front-contact {
    position: absolute;
    left: 262px; top: 210px;
    font-size: 10.5px;
    line-height: 15px;
    color: var(--ink-dark);
    list-style: none;
    white-space: nowrap;
  }
  .front-contact .label { display: inline-block; width: 40px; }

  /* back */
  .back-name {
    position: absolute;
    left: 0; right: 0; top: 182px;
    text-align: center;
    font-size: 21px;
    letter-spacing: 1.5px;
    white-space: nowrap;
    color: var(--ink-dark);
  }
  .back-web {
    position: absolute;
    left: 0; right: 0; top: 250px;
    text-align: center;
    font-size: 11px;
    letter-spacing: 2.5px;
    white-space: nowrap;
    color: var(--ink-dark);
  }
</style>
</head>
<body>
<main class="canvas">

  <section class="card card-front" aria-label="Business card front">
    <svg class="card-shape" viewBox="0 0 492 282" aria-hidden="true">
      <path d="M0 0 H492 V148 Q246 222 0 148 Z" fill="var(--card-white)"/>
    </svg>
    <p class="front-name serif">MARISOL DEVEREUX</p>

    <div class="front-identity serif">
      <p class="person">MARISOL DEVEREUX</p>
      <p class="role">FASHION DESIGNER</p>
    </div>

    <ul class="front-contact sans">
      <li><span class="label">Phone</span>: 0400612347</li>
      <li><span class="label">Email</span>: marisol@marisoldevereux.com</li>
      <li><span class="label">Web</span>: www.marisoldevereux.com</li>
    </ul>
  </section>

  <section class="card card-back" aria-label="Business card back">
    <p class="back-name serif">MARISOL DEVEREUX</p>
    <p class="back-web serif">WWW.MARISOLDEVEREUX.COM</p>
  </section>

</main>
</body>
</html>
```